Professional Actor Training Video for Series Television needs an online flyer design

Corvell Prize Winning actor. DorenTeo Marsh has produced a new pro actor training video that teaches actor's how to audition for and win roles in Series Television and Feature Film. This program is special because it is produced by an actor with 25 years of successful experience who is still actually working in the business. The flyer design should consists primarily of Mr. Marsh name and the program title (which is fairly long) the final design should reflect the value of the program for the serious actor as well as the novice. Please visit Mr. Marsh FLIKDEX page to get a sense of his long career and continued success as a working actor. Final design can include a photo but not necessarily a must

Title:
DorenTeo Marsh'
STILLNESS TIMING and RESONANCE
The Working Performer's Handbook For Landing Parts in Episodic Drama and Motion Pictures

Target Market(s)

Individuals competing for or seeking to compete for roles in Series Television and Feature Film

Industry/Entity Type

Film Production

Requirements
Must have
• Program title and subtitle must large and be the most prominent aspect of the flyer
• Title:
• DorenTeo Marsh'
• STILLNESS TIMING and RESONANCE
• The Working Performer's Handbook For Landing Parts in Episodic Drama and Motion Pictures
Should not have
• Image of Curtains (as on a stage). images of slate, film stock,

```html
<!DOCTYPE html>
<html lang="en">
<head>
<meta charset="utf-8">
<title>DorenTeo Marsh' – Stillness Timing and Resonance</title>
<link href="https://fonts.googleapis.com/css2?family=Oswald:wght@300;400&display=swap" rel="stylesheet">
<style>
  :root{
    --paper:#c9b38c;
    --paper-dark:#b69c72;
    --frame:#d8c49e;
    --frame-edge:#a98f66;
    --bubble:#8d7b5b;
    --bubble-edge:#5e4f38;
    --cream:#f3ead6;
    --ink:#3b3124;
  }
  html,body{margin:0;padding:0;overflow:hidden;background:var(--paper);}
  .flyer{position:relative;width:776px;height:1200px;overflow:hidden;background:var(--paper);}
  .presenter-name{position:absolute;left:0;top:38px;width:776px;margin:0;text-align:center;
    font-family:"Oswald",sans-serif;font-weight:400;font-size:104px;line-height:1;
    letter-spacing:2px;color:var(--ink);}
  .band-line{position:absolute;left:0;width:776px;height:2px;background:var(--frame-edge);opacity:.6;}
  .side-panel{position:absolute;top:232px;height:620px;background:var(--paper-dark);}
  .side-panel.left{left:0;width:173px;}
  .side-panel.right{left:620px;width:156px;}
  .portrait-frame{position:absolute;left:175px;top:245px;width:444px;height:608px;background:var(--frame);
    border:6px dotted var(--frame-edge);box-sizing:border-box;}
  .portrait{position:absolute;left:209px;top:271px;width:378px;height:552px;
    background:radial-gradient(ellipse at 50% 45%,#5a4f45 0%,#2e2925 55%,#161412 100%);}
  .bubble{position:absolute;left:0;top:0;}
  .title-block{position:absolute;left:24px;top:893px;width:729px;text-align:center;color:var(--cream);
    font-family:"Oswald",sans-serif;}
  .program-title{margin:24px 0 0;font-weight:400;font-size:52px;letter-spacing:.3px;line-height:1;}
  .program-title .small{font-size:40px;}
  .program-subtitle{margin:12px 0 0;font-weight:300;font-size:39px;font-variant:small-caps;line-height:70px;letter-spacing:.4px;}
</style>
</head>
<body>
<div class="flyer">
  <h2 class="presenter-name">DorenTeo Marsh'</h2>
  <div class="band-line" style="top:228px"></div>
  <div class="side-panel left" role="img" aria-label="Tan paper texture with fine fibre strands"></div>
  <div class="side-panel right" role="img" aria-label="Tan paper texture with fine fibre strands"></div>
  <div class="band-line" style="top:852px"></div>
  <div class="portrait-frame"></div>
  <div class="portrait" role="img" aria-label="Black and white headshot portrait of DorenTeo Marsh"></div>

  <svg class="bubble" width="776" height="1200" viewBox="0 0 776 1200">
    <path d="M56 893 H721 Q753 893 753 925 V1085 Q753 1117 721 1117 H640 L612 1198 L598 1117 H56 Q24 1117 24 1085 V925 Q24 893 56 893 Z"
      fill="var(--bubble)" stroke="var(--bubble-edge)" stroke-width="3"/>
  </svg>
  <div class="title-block">
    <h1 class="program-title">STILLNESS TIMING <span class="small">and</span> RESONANCE</h1>
    <p class="program-subtitle">The Working Performer’s Handbook For Landing Parts<br>in Episodic Drama and Motion Pictures</p>
  </div>
</div>
</body>
</html>
```